Marlow Cat Lodge needs a website and a logo :)

I need a web design for my pet hotel. I will use it in Wordpress, probable with Elementor, so if you can also offer the WP template creation, that's a bonus but I don't wanna book the coded-website option here as I don't think that applies to WP. It would be great if you come up with a logo as well.

Here some info:

Modern, premium cat boarding with a vet on-site

Marlow Cat Lodge is a boutique cat boarding facility in Ashby Vale, Corland, offering high-quality, vet-supervised care for all cats, including those with special medical needs. Unlike standard catteries, we focus on low-stress boarding, with separate spaces for special-needs and healthy cats, ensuring a safe, comfortable, and peaceful environment. We also prioritize convenience with self check-in and check-out, leveraging technology to enhance the experience.

Target Market(s)

Cat owners for short term to long term stays that don't want the cheapest option and will value that we have a vet on-site

Industry/Entity Type

cat boarding

Number of Pages Required

5+ page

Font styles to use
Sans Serif
Other font styles liked:
• Nothing that needs installation or a license. Please use Google Fonts.

Requirements
Must have
• Landing page, about us, services, blog and contact page - the landing page should have the typical sales layout with hero image top right, a tag line "Modern, premium cat boarding with a vet on-site" and 2 paragraphs. Paragraph 1 (Problem): Leaving your cat behind can be stressful, especially if they need special care. Standard catteries often lack vet oversight and a calm, tailored environment. Paragraph 2 (Solution): At Marlow Cat Lodge, we offer premium, vet-supervised boarding with separate spaces for special-needs and healthy cats. Our self check-in and tech-driven system makes drop-offs and pick-ups effortless... you know the drill :)
Nice to have
• Ask ChatGPT for some ideas and give it the business plan: https://files.example-docs.net/document/d/7qerTy_LKMWBP2hfsx8V304UiLoXyOpqRkZjTnWaBcD/edit?usp=sharing
Should not have
• NO DOGS :)

```html
<!DOCTYPE html>
<html lang="en">
<head>
<meta charset="utf-8">
<title>Marlow Cat Lodge</title>
<link href="https://fonts.googleapis.com/css2?family=Lato:wght@400;700;900&display=swap" rel="stylesheet">
<style>
:root{
  --blue:#1a8ad4;
  --green:#6aab3a;
  --ink:#1f1f1f;
  --text:#444;
  --muted:#666;
  --footer:#0b0b0b;
  --white:#fff;
}
*{margin:0;padding:0;box-sizing:border-box}
html,body{width:1200px;height:4187px;overflow:hidden;background:#fff}
body{position:relative;font-family:'Lato',sans-serif;color:var(--text)}
.abs{position:absolute}
.blue{color:var(--blue)}
.green{color:var(--green)}
.btn{position:absolute;display:flex;align-items:center;justify-content:center;background:var(--green);color:#fff;font-weight:700;font-size:15px;border-radius:3px}
.section-title{position:absolute;left:0;width:1200px;text-align:center;font-size:42px;font-weight:700;color:var(--ink);line-height:1}
.photo{position:absolute;border-radius:4px}

/* header */
.brand{left:110px;top:34px;font-size:39px;font-weight:700;color:var(--ink);line-height:1}
.nav a{position:absolute;top:48px;font-size:14.5px;color:#333;text-decoration:none;line-height:18px}
.nav .active{left:463px;top:41px;width:57px;height:32px;background:var(--green);color:#fff;border-radius:3px;display:flex;align-items:center;justify-content:center}
.book-now{left:941px;top:34px;width:147px;height:42px;background:var(--blue);font-size:15px}

/* hero */
.hero{left:34px;top:114px;width:1132px;height:616px;border-radius:18px;overflow:hidden;
  background:linear-gradient(90deg,#2c2622 0%,#4a3b30 35%,#6f7f93 58%,#8fa7c2 72%,#5b4636 100%)}
.hero-shade{position:absolute;inset:0;background:linear-gradient(90deg,rgba(20,16,13,.7) 0%,rgba(20,16,13,.35) 50%,rgba(0,0,0,0) 70%)}
.hero h1{position:absolute;left:73px;top:86px;width:470px;font-size:42px;font-weight:900;line-height:54px;color:#fff}
.hero .label{position:absolute;left:76px;font-size:14.5px;font-weight:700;color:#fff}
.hero p{position:absolute;left:76px;font-size:14.5px;line-height:20.5px;color:#fff}
.dots{position:absolute;left:531px;top:537px;display:flex;gap:8px}
.dots span{width:11px;height:11px;border-radius:50%;background:rgba(255,255,255,.45)}
.dots span:first-child{background:#fff}

/* why */
.why-col{position:absolute;top:880px;width:300px;text-align:center}
.why-col svg{display:block;margin:0 auto}
.why-col h3{margin-top:28px;font-size:21px;font-weight:700;color:var(--blue);line-height:1}
.why-col p{margin:14px auto 0;width:240px;font-size:14.5px;line-height:20.5px;color:var(--text)}

/* about */
.about-text{left:644px;width:450px;font-size:14.5px;line-height:23px;color:var(--text)}

/* services */
.svc{position:absolute;top:1792px;width:303px;text-align:center}
.svc .photo{position:relative;width:303px;height:255px;display:block}
.svc h3{margin-top:28px;font-size:22px;font-weight:700;color:var(--blue);line-height:1}
.svc p{margin-top:14px;font-size:14.5px;line-height:22px;color:var(--text)}
.svc .btn{position:relative;margin:22px auto 0;width:142px;height:43px}
.arrow{position:absolute;width:30px;height:30px;border-radius:50%;background:var(--blue);display:flex;align-items:center;justify-content:center}

/* cta */
.cta{left:49px;top:2322px;width:1102px;height:384px;border-radius:12px;background:linear-gradient(135deg,#1d7fc4,#1a8ad4 60%,#2a98dc)}
.cta h2{position:absolute;top:80px;width:100%;text-align:center;font-size:42px;font-weight:700;color:#fff;line-height:1}
.cta .sub{position:absolute;top:142px;width:100%;text-align:center;font-size:20px;color:#fff}
.cta .small{position:absolute;top:180px;width:100%;text-align:center;font-size:15px;line-height:22px;color:#fff}

/* reviews */
.review{position:absolute;top:2899px;width:318px;height:228px;border:1px solid #eee;border-radius:4px;background:#fff;padding:30px 24px 0}
.review.featured{background:var(--green);border-color:var(--green)}
.stars{display:flex;gap:2px}
.review p{margin-top:20px;font-size:14.5px;line-height:22px;color:var(--text)}
.review .name{margin-top:18px;font-size:17px;color:var(--blue)}
.review .date{margin-top:6px;font-size:13px;color:#555}
.review.featured p,.review.featured .name,.review.featured .date{color:#fff}

/* blog */
.thumb{position:absolute;top:3572px;width:157px;height:101px;border-radius:3px}

/* footer */
.footer{left:0;top:3759px;width:1200px;height:428px;background:var(--footer)}
.footer h4{position:absolute;top:88px;font-size:20px;font-weight:700;color:#fff}
.footer .txt{position:absolute;font-size:14.5px;line-height:26px;color:#fff}
.social{position:absolute;top:275px;width:34px;height:34px;border-radius:5px;border:2px solid #fff}
.social.on{background:var(--green);border-color:var(--green)}
.rule{position:absolute;left:112px;top:373px;width:976px;height:1px;background:#333}
.copy{position:absolute;top:400px;width:1200px;text-align:center;font-size:12.5px;color:#fff}
</style>
</head>
<body>

<header>
  <div class="abs brand">Marlow Cat Lodge</div>
  <nav class="nav">
    <a class="active" href="#">Home</a>
    <a href="#" style="left:558px">About Us</a>
    <a href="#" style="left:665px">Services</a>
    <a href="#" style="left:766px">Blog</a>
    <a href="#" style="left:841px">Contact Us</a>
  </nav>
  <div class="btn book-now">Book Now</div>
</header>

<section class="abs hero" role="img" aria-label="Cat walking on a wooden floor while its owner reaches down to stroke it">
  <div class="hero-shade"></div>
  <h1>Modern, Premium Cat Boarding with a Vet On-Site</h1>
  <div class="label" style="top:267px">Problem :</div>
  <p style="top:293px;width:480px">Leaving your cat behind can be stressful, especially if they need special care. Standard catteries often lack vet oversight and a calm, tailored environment.</p>
  <div class="label" style="top:376px">Solution :</div>
  <p style="top:402px;width:540px">At Marlow Cat Lodge, we offer premium, vet-supervised boarding with separate spaces for special-needs and healthy cats. Our self check-in and tech-driven system makes drop-offs and pick-ups effortless... you know the drill :)</p>
  <div class="btn" style="left:78px;top:489px;width:147px;height:43px">Book Now</div>
  <div class="dots"><span></span><span></span><span></span><span></span></div>
</section>

<section class="why">
  <div class="section-title" style="top:812px">Why Choose <span class="blue">Marlow Cat Lodge?</span></div>
  <div class="why-col" style="left:79px">
    <svg width="96" height="96" viewBox="0 0 96 96" fill="none" stroke="#6aab3a" stroke-width="3" stroke-linejoin="round">
      <circle cx="48" cy="60" r="30" fill="#eef0ec" stroke="none"/>
      <path d="M10 8h44v32H28l-10 10v-10h-8z"/>
      <path d="M28 16v16M20 24h16"/>
      <path d="M46 46h40v32H72l-8 10v-10H46z"/>
      <circle cx="60" cy="66" r="3"/><circle cx="70" cy="66" r="3"/><circle cx="56" cy="58" r="2.5"/><circle cx="74" cy="58" r="2.5"/>
    </svg>
    <h3>Vet-Supervised Care</h3>
    <p>A qualified vet is on-site to ensure your cat's health and well-being. Perfect for both healthy and special-needs cats.</p>
  </div>
  <div class="why-col" style="left:452px">
    <svg width="96" height="96" viewBox="0 0 96 96" fill="none" stroke="#6aab3a" stroke-width="3" stroke-linejoin="round">
      <circle cx="48" cy="60" r="30" fill="#eef0ec" stroke="none"/>
      <circle cx="48" cy="28" r="20"/><circle cx="48" cy="28" r="14"/>
      <path d="M52 20h-6a4 4 0 0 0 0 8h4a4 4 0 0 1 0 8h-6M48 16v4M48 36v4"/>
      <path d="M14 44v30l10 10M82 44v30l-10 10M34 56v20l-6 6M62 56v20l6 6"/>
    </svg>
    <h3>Low-Stress Boarding</h3>
    <p>Unlike standard catteries, we offer separate spaces for special-needs and healthy cats, creating a peaceful environment.</p>
  </div>
  <div class="why-col" style="left:830px">
    <svg width="96" height="96" viewBox="0 0 96 96" fill="none" stroke="#6aab3a" stroke-width="3" stroke-linejoin="round">
      <circle cx="48" cy="60" r="30" fill="#eef0ec" stroke="none"/>
      <path d="M48 44c-12-8-18-14-18-22a9 9 0 0 1 18-3 9 9 0 0 1 18 3c0 8-6 14-18 22z"/>
      <path d="M14 30v30l14 12v8M82 30v30l-14 12v8"/>
      <path d="M20 80h16v8H20zM60 80h16v8H60z"/>
    </svg>
    <h3>Premium Comfort</h3>
    <p>Excepteur sint occaecat cupidatat non proident, sunt in culpa qui officia deserunt mollit anim id est laborum."</p>
  </div>
</section>

<section class="about">
  <div class="photo" style="left:112px;top:1197px;width:436px;height:437px;background:linear-gradient(160deg,#d9dadb,#a9a8a4 55%,#6c635a)" role="img" aria-label="Cat behind a glass door touching a person's outstretched hand"></div>
  <div class="abs" style="left:644px;top:1190px;font-size:42px;font-weight:700;color:var(--ink)">About <span class="blue">Us</span></div>
  <p class="abs about-text" style="top:1264px">Marlow Cat Lodge is a boutique cat boarding facility in Ashby Vale, Corland, offering premium, vet-supervised care in a calm, stress-free environment. We know that leaving your cat behind can be difficult—especially if they have special medical needs. That's why we've designed a safe, comfortable, and personalized experience to give both you and your cat peace of mind.</p>
  <p class="abs about-text" style="top:1436px">At Marlow Cat Lodge, we go beyond traditional catteries to offer a high-end, stress-free boarding experience. Whether your cat is young and playful or requires extra medical attention, our customized care approach ensures their stay is as comfortable as possible.</p>
  <div class="btn" style="left:644px;top:1592px;width:143px;height:42px">Read More</div>
</section>

<section class="services">
  <div class="section-title" style="top:1718px">Our <span class="green">Services</span></div>
  <div class="arrow" style="left:61px;top:1906px"><svg width="14" height="14" viewBox="0 0 14 14"><path d="M9 2 4 7l5 5" stroke="#fff" stroke-width="2.2" fill="none"/></svg></div>
  <div class="arrow" style="left:1108px;top:1906px"><svg width="14" height="14" viewBox="0 0 14 14"><path d="M5 2l5 5-5 5" stroke="#fff" stroke-width="2.2" fill="none"/></svg></div>
  <div class="svc" style="left:112px">
    <div class="photo" style="background:linear-gradient(160deg,#c9c2b6,#7d95b0 55%,#5f6f83)" role="img" aria-label="Carer in a denim shirt holding a cat on her lap"></div>
    <h3>Premium Cat Boarding</h3>
    <p>Lorem ipsum dolor sit amet, consectetur adipiscing elit, sed do eiusmod tempor incididt ut labore et dolore magna aliqua.</p>
    <div class="btn">Read More</div>
  </div>
  <div class="svc" style="left:449px">
    <div class="photo" style="background:linear-gradient(160deg,#e4e2df,#b9b5b0 55%,#8c8580)" role="img" aria-label="Fluffy cat sitting in a white cat house"></div>
    <h3>Self Check-in &amp; Check-out</h3>
    <p>Lorem ipsum dolor sit amet, consectetur adipiscing elit, sed do eiusmod tempor incididt ut labore et dolore magna aliqua.</p>
    <div class="btn">Read More</div>
  </div>
  <div class="svc" style="left:785px">
    <div class="photo" style="background:linear-gradient(160deg,#e8d9bf,#d7c8b4 50%,#a6988a)" role="img" aria-label="Woman sitting on the floor holding a cat"></div>
    <h3>Pet Transport Services</h3>
    <p>Lorem ipsum dolor sit amet, consectetur adipiscing elit, sed do eiusmod tempor incididt ut labore et dolore magna aliqua.</p>
    <div class="btn">Read More</div>
  </div>
</section>

<section class="abs cta">
  <h2>Ready to Give Your Cat the Best Stay?</h2>
  <div class="sub">Book a premium, stress-free stay with expert vet care today!</div>
  <div class="small">A safe, stress-free, and comfortable stay for your cat. Self check-in,<br>vet-supervised care, and luxury accommodations.</div>
  <div class="btn" style="left:450px;top:254px;width:202px;height:42px">Book Your Cat's Stay</div>
</section>

<section class="reviews">
  <div class="section-title" style="top:2818px">What Our <span class="blue">Customers Say</span></div>
  <div class="review" style="left:111px">
    <div class="stars"><svg width="74" height="14" viewBox="0 0 74 14"><g fill="#f08a1c"><path id="s" d="M7 0l2 4.5 5 .5-3.8 3.3 1.1 4.9L7 10.6 2.7 13.2l1.1-4.9L0 5l5-.5z"/><use href="#s" x="15"/><use href="#s" x="30"/><use href="#s" x="45"/><use href="#s" x="60"/></g></svg></div>
    <p>Excepteur sint occaecat cupidatat non proident, sunt in culpa qui officia deserunt mollit anim id est laborum.</p>
    <div class="name">Hargreave</div>
    <div class="date">Feb 27 2024</div>
  </div>
  <div class="review featured" style="left:441px">
    <div class="stars"><svg width="74" height="14" viewBox="0 0 74 14"><g fill="#fff"><use href="#s"/><use href="#s" x="15"/><use href="#s" x="30"/><use href="#s" x="45"/><use href="#s" x="60"/></g></svg></div>
    <p>Excepteur sint occaecat cupidatat non proident, sunt in culpa qui officia deserunt mollit anim id est laborum.</p>
    <div class="name">Elena</div>
    <div class="date">Feb 27 2024</div>
  </div>
  <div class="review" style="left:771px">
    <div class="stars"><svg width="74" height="14" viewBox="0 0 74 14"><g fill="#f08a1c"><use href="#s"/><use href="#s" x="15"/><use href="#s" x="30"/><use href="#s" x="45"/><use href="#s" x="60"/></g></svg></div>
    <p>Excepteur sint occaecat cupidatat non proident, sunt in culpa qui officia deserunt mollit anim id est laborum.</p>
    <div class="name">Rosalind</div>
    <div class="date">Feb 27 2024</div>
  </div>
</section>

<section class="blog">
  <div class="abs" style="left:112px;top:3210px;font-size:42px;font-weight:700;color:var(--ink)">Our <span class="blue">Blog</span></div>
  <div class="abs green" style="left:112px;top:3280px;font-size:21px;font-weight:700">Cat Care Tips, Boarding Advice &amp; More!</div>
  <p class="abs" style="left:112px;top:3330px;width:450px;font-size:14.5px;line-height:23px">At Marlow Cat Lodge, we go beyond traditional catteries to offer a high-end, stress-free boarding experience. Whether your cat is young and playful or requires extra medical attention, our customized care approach ensures their stay is as comfortable as possible.</p>
  <div class="btn" style="left:112px;top:3483px;width:142px;height:42px">Read More</div>
  <div class="photo" style="left:652px;top:3215px;width:436px;height:439px;background:linear-gradient(135deg,#f1efec,#d9d4cf 50%,#c9b8a6)" role="img" aria-label="Woman beside white cat suites with a ginger cat climbing inside"></div>
  <div class="thumb" style="left:111px;background:linear-gradient(135deg,#5e8fc2,#9fbfdc)" role="img" aria-label="Carer with a cat in a blue-lit room"></div>
  <div class="thumb" style="left:298px;background:linear-gradient(135deg,#f2f0ec,#d7cdc0)" role="img" aria-label="Carer holding a cat"></div>
  <div class="thumb" style="left:483px;background:linear-gradient(135deg,#b3aea7,#6d6760)" role="img" aria-label="Cat suites in a boarding room"></div>
  <div class="thumb" style="left:670px;background:linear-gradient(135deg,#8a7b72,#4f6a8a)" role="img" aria-label="Two carers attending to a cat"></div>
  <div class="arrow" style="left:121px;top:3606px;background:rgba(255,255,255,.85)"><svg width="14" height="14" viewBox="0 0 14 14"><path d="M9 2 4 7l5 5" stroke="#1a8ad4" stroke-width="2.2" fill="none"/></svg></div>
  <div class="arrow" style="left:783px;top:3606px;background:rgba(255,255,255,.9)"><svg width="14" height="14" viewBox="0 0 14 14"><path d="M5 2l5 5-5 5" stroke="#1a8ad4" stroke-width="2.2" fill="none"/></svg></div>
</section>

<footer class="abs footer">
  <h4 style="left:114px">About Us</h4>
  <div class="txt" style="left:112px;top:126px;width:270px">Low-stress, luxury boarding for all cats, including those with special medical needs. Safe, comfortable, and effortless with self check-in &amp; check-out.</div>
  <div class="social on" style="left:113px"></div>
  <div class="social" style="left:162px;width:22px;height:22px;top:281px"></div>
  <div class="social" style="left:209px;width:22px;height:22px;top:281px"></div>
  <div class="social" style="left:256px;width:24px;height:22px;top:281px"></div>

  <h4 style="left:455px">Contact Us</h4>
  <svg class="abs" style="left:455px;top:130px" width="18" height="22" viewBox="0 0 18 22" fill="none" stroke="#fff" stroke-width="1.6"><path d="M9 21s7-7 7-12A7 7 0 0 0 2 9c0 5 7 12 7 12z"/><circle cx="9" cy="9" r="2.5"/></svg>
  <div class="txt" style="left:494px;top:126px;width:200px">48, Cat boarding facility in Ashby Vale, Corland AV 0000.</div>
  <svg class="abs" style="left:455px;top:238px" width="18" height="18" viewBox="0 0 18 18" fill="none" stroke="#fff" stroke-width="1.6"><path d="M4 1l3 4-2 2c1 2 3 4 5 5l2-2 4 3-2 3C8 16 2 10 1 4z"/></svg>
  <div class="txt" style="left:494px;top:235px">+ 1 555 014 2290</div>
  <svg class="abs" style="left:455px;top:288px" width="19" height="15" viewBox="0 0 19 15" fill="none" stroke="#fff" stroke-width="1.6"><rect x="1" y="1" width="17" height="13" rx="1.5"/><path d="M1 2l8.5 6L18 2"/></svg>
  <div class="txt" style="left:494px;top:283px">info@marlowcatlodge.example</div>

  <h4 style="left:785px">Quick Links</h4>
  <div class="txt" style="left:786px;top:126px;line-height:38.5px">Home<br>About Us<br>Services<br>Blog<br>Contact Us</div>

  <h4 style="left:977px">Other Links</h4>
  <div class="txt" style="left:977px;top:126px;line-height:38.5px">FAQ<br>Reviews<br>Support<br>Privacy Policy<br>Terms of Service</div>

  <div class="rule"></div>
  <div class="copy">Copyright © 2025 Marlow Cat Lodge. All Rights Reserved.</div>
</footer>

</body>
</html>
```